An insurance broker wants to represent the company's vision visually and textually.

My company, with a total of 10 employees, developed a vision this year. Now, we want to display this vision in the form of a two-meter-high visual that will be mounted on the wall. This ensures that the vision is always visible to our employees, as well as to our clients and partners when they visit our office.

Here's my idea: the vision will be accompanied by a fitting image, with the text of the vision itself elegantly written in a beautiful font. Our vision reads: "Every company always has a perfectly tailored future solution for greater financial security, freedom, and joy."

A bit about my company: we are an insurance broker, and our services are primarily designed for corporate clients.

```html
<!DOCTYPE html>
<html lang="en">
<head>
<meta charset="UTF-8">
<title>Vision Wall Visual</title>
<link rel="stylesheet" href="https://fonts.googleapis.com/css2?family=Playfair+Display:wght@800&family=Yellowtail&family=League+Spartan:wght@700&display=swap">
<style>
  :root {
    --paper: #ffffff;
    --ink-dark: #383838;
    --ink-mid: #666666;
    --ink-soft: #7a7a7a;
    --bracket: #696969;
    --art-a: #3a3a3a;
    --art-b: #858585;
  }
  html, body {
    margin: 0;
    padding: 0;
    width: 1200px;
    height: 1200px;
    overflow: hidden;
    background: var(--paper);
  }
  .vision-board {
    display: block;
    width: 1200px;
    height: 1200px;
  }
  .headline-serif {
    font-family: "Playfair Display", serif;
    font-weight: 800;
    fill: var(--ink-mid);
  }
  .connector-script {
    font-family: "Yellowtail", cursive;
    fill: var(--ink-soft);
  }
  .closing-sans {
    font-family: "League Spartan", sans-serif;
    font-weight: 700;
    fill: var(--ink-dark);
  }
  .frame-corner {
    fill: none;
    stroke: var(--bracket);
    stroke-width: 8;
  }
</style>
</head>
<body>
<svg class="vision-board" viewBox="0 0 1200 1200" xmlns="http://www.w3.org/2000/svg">
  <defs>
    <linearGradient id="puzzleTone" x1="0" y1="0" x2="1" y2="0">
      <stop offset="0" stop-color="var(--art-a)"/>
      <stop offset="1" stop-color="var(--art-b)"/>
    </linearGradient>
  </defs>

  <rect class="puzzle-artwork" x="330" y="56" width="550" height="328" fill="url(#puzzleTone)"
        role="img" aria-label="Pyramid of interlocking puzzle pieces in shades of grey"/>

  <g class="frame">
    <path class="frame-corner" d="M117 466 V395 H191"/>
    <path class="frame-corner" d="M1019 395 H1093 V466"/>
    <path class="frame-corner" d="M117 1094 V1165 H191"/>
    <path class="frame-corner" d="M1019 1165 H1093 V1094"/>
  </g>

  <g class="vision-statement">
    <text class="headline-serif" x="208" y="509" font-size="96" textLength="792" lengthAdjust="spacingAndGlyphs">EVERY COMPANY</text>
    <text class="connector-script" x="459" y="583" font-size="52" textLength="291" lengthAdjust="spacingAndGlyphs">always has a</text>
    <text class="headline-serif" x="142" y="678" font-size="76" textLength="926" lengthAdjust="spacingAndGlyphs">PERFECTLY TAILORED</text>
    <text class="headline-serif" x="277" y="757" font-size="66" textLength="664" lengthAdjust="spacingAndGlyphs">FUTURE SOLUTION</text>
    <text class="connector-script" x="475" y="815" font-size="52" textLength="259" lengthAdjust="spacingAndGlyphs">for greater</text>
    <text class="closing-sans" x="378" y="928" font-size="94" textLength="456" lengthAdjust="spacingAndGlyphs">FINANCIAL</text>
    <text class="closing-sans" x="180" y="1027" font-size="94" textLength="848" lengthAdjust="spacingAndGlyphs">SECURITY, FREEDOM</text>
    <text class="closing-sans" x="414" y="1119" font-size="94" textLength="379" lengthAdjust="spacingAndGlyphs">AND JOY.</text>
  </g>
</svg>
</body>
</html>
```